Boutique Sparkling Blanc de Blancs Wine label

We are looking for a label and neck label for our new Sparkling Chardonnay.
Images uploaded include, bubbles and glitter maybe as a faded background for whole label?
We like Refined, elegant yet simple designs.
Have included our current table chardonnay label as example.

Industry/Entity Type

Boutique

Font styles to use
Decorative
Script

Requirements
Must have
• Name - "Every Moonlit Hour"
• Methode Traditionelle
• Blanc de Blancs
• 2015
• Beyond the Orchards (Brand)
• Adelaide Hills
Nice to have
• Neutral tones
• Sparkles, Glitter, Bubbles
• Traditional, cursive or vine like fonts
• Have attached fonts we used for previous wine label - might be nice to carry through same/similar fonts to continue our brand?
Should not have
• a lot of colour

```html
<!DOCTYPE html>
<html lang="en">
<head>
<meta charset="utf-8">
<title>Every Moonlit Hour – Blanc de Blancs Label</title>
<link rel="stylesheet" href="https://fonts.googleapis.com/css2?family=Great+Vibes&family=Kaushan+Script&display=swap">
<style>
  :root {
    --canvas: #ffffff;
    --neck-black: #0c0c0c;
    --gold-dark: #5e4a1a;
    --gold-mid: #a88a3a;
    --gold-light: #e2cf8a;
    --label-cream: #f3f0ea;
    --label-grey: #d9d5cd;
    --frame-line: #8d8778;
    --varietal-red: #b3123a;
    --vintage-ink: #151515;
    --band-text: #f6f2e6;
  }
  * { margin: 0; padding: 0; box-sizing: border-box; }
  html, body {
    width: 1200px;
    height: 1200px;
    overflow: hidden;
    background: var(--canvas);
  }
  .canvas {
    width: 1200px;
    height: 1200px;
    display: flex;
    flex-direction: column;
    align-items: center;
    justify-content: center;
    gap: 60px;
  }

  /* Neck label */
  .neck-label {
    position: relative;
    width: 420px;
    height: 190px;
  }
  .neck-label svg { position: absolute; inset: 0; }
  .neck-ornament {
    position: absolute;
    left: 160px;
    top: 22px;
    width: 100px;
    height: 62px;
    border-radius: 40% 40% 50% 50%;
    background: radial-gradient(circle at 50% 45%, var(--gold-light), var(--gold-mid) 55%, var(--gold-dark));
  }
  .neck-name {
    position: absolute;
    left: 0;
    right: 0;
    top: 92px;
    text-align: center;
    font-family: "Great Vibes", cursive;
    font-weight: 400;
    font-size: 30px;
    color: var(--gold-light);
  }

  /* Main label */
  .main-label {
    position: relative;
    width: 660px;
    height: 600px;
    background:
      radial-gradient(circle at 70% 20%, rgba(255,255,255,0.9), transparent 40%),
      radial-gradient(circle at 25% 60%, rgba(255,255,255,0.75), transparent 35%),
      radial-gradient(circle at 85% 75%, rgba(200,190,170,0.35), transparent 40%),
      linear-gradient(160deg, var(--label-cream), var(--label-grey) 60%, var(--label-cream));
  }
  .label-frame {
    position: absolute;
    left: 20px;
    right: 20px;
    top: 20px;
    height: 480px;
    border: 2px solid var(--frame-line);
  }
  .wine-name {
    position: absolute;
    left: 40px;
    right: 40px;
    top: 58px;
    text-align: center;
    font-family: "Kaushan Script", cursive;
    font-weight: 400;
    font-size: 84px;
    line-height: 1.12;
    transform: rotate(-4deg);
    background: linear-gradient(100deg, var(--gold-dark), var(--gold-mid) 30%, var(--gold-light) 50%, var(--gold-mid) 70%, var(--gold-dark));
    -webkit-background-clip: text;
    background-clip: text;
    color: transparent;
  }
  .wine-name span { display: block; }
  .wine-name .line-one { margin-left: -20px; }
  .wine-name .line-two { margin-left: 60px; }
  .varietal {
    position: absolute;
    left: 0;
    right: 0;
    top: 350px;
    text-align: center;
    font-family: "Great Vibes", cursive;
    font-weight: 400;
    font-size: 54px;
    color: var(--varietal-red);
  }
  .vintage {
    position: absolute;
    left: 0;
    right: 0;
    top: 420px;
    text-align: center;
    font-family: "Kaushan Script", cursive;
    font-weight: 400;
    font-size: 50px;
    color: var(--vintage-ink);
  }
  .region-band {
    position: absolute;
    left: 0;
    right: 0;
    bottom: 28px;
    height: 64px;
    background: linear-gradient(90deg, var(--gold-dark), var(--gold-mid) 25%, #8a7a4c 50%, var(--gold-mid) 75%, var(--gold-dark));
    display: flex;
    align-items: center;
    justify-content: center;
    font-family: "Great Vibes", cursive;
    font-weight: 400;
    font-size: 44px;
    color: var(--band-text);
  }
  .base-rule {
    position: absolute;
    left: 0;
    right: 0;
    bottom: 12px;
    height: 8px;
    background: var(--neck-black);
  }
</style>
</head>
<body>
<main class="canvas">
  <section class="neck-label" aria-label="Neck label">
    <svg width="420" height="190" viewBox="0 0 420 190">
      <path d="M0 0 H420 V130 Q210 220 0 130 Z" fill="var(--neck-black)"/>
      <path d="M110 150 Q210 175 310 150" fill="none" stroke="var(--gold-mid)" stroke-width="2"/>
    </svg>
    <div class="neck-ornament" role="img" aria-label="Gold grapevine cluster ornament"></div>
    <p class="neck-name">Every Moonlit Hour</p>
  </section>

  <section class="main-label" aria-label="Front label">
    <div class="label-frame"></div>
    <h1 class="wine-name">
      <span class="line-one">Every Moonlit</span>
      <span class="line-two">Hour</span>
    </h1>
    <p class="varietal">Blanc de Blancs</p>
    <p class="vintage">2015</p>
    <div class="region-band">Adelaide Hills</div>
    <div class="base-rule"></div>
  </section>
</main>
</body>
</html>
```